ecommerce website design for pool store

I need a homepage designed for an e-commerce store for a pool shop. It will be similar to https://www.aquabrite.com.au/ but not an exact copy (ie. the icons, photos and colour scheme need to be different). aquabrite.com.au is one of our competitors but we love everything about their website.
I have attached the logo for this site. We want the background to be white and the colours used on the site to be the blue from the logo and the blue and green used on www.hopscotchyouth.com.au
I want the same layout for the logo, search and menu bar at the top along with the 'shop filter cartidges' feature button
Under that a similar slideshow
Under that, the categories with the logos, the best sellers, trending now (but call this 'latest products') and all the other same elements as on this example site.

```html
<!DOCTYPE html>
<html lang="en">
<head>
<meta charset="utf-8">
<title>Pool Haven – Pool Store</title>
<link href="https://fonts.googleapis.com/css2?family=Montserrat:wght@500;600;700;800;900&family=Nunito+Sans:wght@400;600;700&display=swap" rel="stylesheet">
<style>
:root{
  --navy:#1b3160;
  --blue:#0aa2e8;
  --sky:#00a6eb;
  --accent:#1ea2e2;
  --text:#22304a;
  --muted:#4a5568;
  --line:#d9e1ea;
  --white:#ffffff;
}
*{box-sizing:border-box;margin:0;padding:0}
html,body{width:1200px;height:2826px;overflow:hidden;background:var(--white)}
body{position:relative;font-family:"Nunito Sans",sans-serif;color:var(--text)}
.abs{position:absolute}
.heading{font-family:"Montserrat",sans-serif;font-weight:800;color:var(--navy);text-align:center;font-size:23px;letter-spacing:.2px}
.heading::after{content:"";display:block;width:32px;height:3px;background:var(--accent);margin:14px auto 0}

/* top bar */
.topbar{left:0;top:0;width:1200px;height:31px;background:var(--navy);color:#fff;font-size:11px;font-family:"Montserrat",sans-serif;font-weight:500;display:flex;justify-content:flex-end;align-items:center;gap:24px;padding-right:132px}
.topbar span{display:flex;align-items:center;gap:7px}
.topbar svg{width:18px;height:18px}

/* header */
.header{left:0;top:31px;width:1200px;height:97px;background:#fff}
.logo-ring{left:122px;top:39px;width:136px;height:136px;border-radius:50%;background:#fff}
.logo{left:130px;top:47px;width:120px;height:120px;border-radius:50%;border:3px solid #1f58b5;display:flex;flex-direction:column;align-items:center;justify-content:center;font-family:"Montserrat",sans-serif;font-weight:700;color:#1f58b5;font-size:13px;letter-spacing:1px;z-index:3}
.search{left:273px;top:48px;width:383px;height:33px;border:1px solid #9aa6b5;border-radius:17px;font-size:10px;color:#555;padding:10px 12px}
.search-btn{left:617px;top:48px;width:39px;height:33px;border-radius:17px;background:var(--blue);display:flex;align-items:center;justify-content:center}
.shop-btn{left:666px;top:48px;width:189px;height:33px;border-radius:17px;background:var(--blue);color:#fff;font-family:"Montserrat",sans-serif;font-weight:700;font-size:12px;display:flex;align-items:center;justify-content:center}
.login{left:868px;top:54px;display:flex;align-items:center;gap:7px;font-family:"Montserrat",sans-serif;font-weight:600;font-size:11px;color:var(--navy)}
.divider{left:978px;top:50px;width:1px;height:32px;background:#ccc}
.cart{left:994px;top:46px;display:flex;align-items:flex-end;gap:6px;font-family:"Montserrat",sans-serif;font-weight:600;font-size:12px;color:var(--navy)}
.cart-count{left:1052px;top:44px;width:16px;height:16px;border-radius:50%;background:var(--blue);color:#fff;font-size:9px;display:flex;align-items:center;justify-content:center;font-weight:700}
.nav{left:273px;top:99px;width:795px;display:flex;justify-content:space-between;font-family:"Montserrat",sans-serif;font-weight:600;font-size:12px;color:#1c2430}

/* hero */
.hero{left:0;top:128px;width:1200px;height:472px;background:linear-gradient(100deg,#a9d3f2 0%,#d8ecfb 40%,#bfe0f7 65%,#5aa8e4 100%)}
.hero-art{left:700px;top:128px;width:500px;height:472px;background:linear-gradient(160deg,rgba(255,255,255,.0),rgba(255,255,255,.55) 45%,rgba(37,120,210,.55) 100%)}
.hero-box{left:227px;top:223px;width:387px;height:241px;border:3px solid var(--navy);border-radius:18px;text-align:center;padding-top:26px}
.hero-box h1{font-family:"Montserrat",sans-serif;font-weight:900;font-size:38px;color:var(--navy);letter-spacing:.5px}
.hero-box p{font-size:17px;line-height:24px;color:#1c2430;margin-top:12px}
.hero-btn{display:inline-block;margin-top:16px;background:var(--navy);color:#fff;font-family:"Montserrat",sans-serif;font-weight:800;font-size:17px;padding:13px 27px;border-radius:22px}
.hero-arrow{top:348px;width:31px;height:33px;background:var(--navy);display:flex;align-items:center;justify-content:center}

/* categories */
.cat{width:303px;height:84px;background:#fff;border-radius:28px;box-shadow:0 2px 14px rgba(30,50,90,.10);display:flex;align-items:center;justify-content:space-between;padding:0 20px 0 24px;font-family:"Montserrat",sans-serif;font-weight:500;font-size:15px;color:var(--navy)}
.cat .thumb{width:78px;height:64px;border-radius:10px}

/* products */
.card{width:182px;height:297px;border:1.5px solid var(--line);border-radius:4px;text-align:center}
.card .pimg{width:140px;height:135px;margin:22px auto 0;border-radius:12px}
.card .pname{font-size:13px;line-height:16px;color:#1c2430;margin-top:24px}
.card .price{font-family:"Montserrat",sans-serif;font-weight:500;font-size:17px;margin-top:9px;color:#111}
.card .add{display:inline-block;margin-top:12px;background:var(--blue);color:#fff;font-family:"Montserrat",sans-serif;font-weight:700;font-size:11px;padding:5px 11px;border-radius:4px}
.circle-arrow{width:30px;height:30px;border:1.5px solid var(--navy);border-radius:50%;display:flex;align-items:center;justify-content:center}

/* features */
.features{left:0;top:1973px;width:1200px;height:263px;background:var(--navy)}
.feature{width:210px;text-align:center;color:#fff}
.feature h3{font-family:"Montserrat",sans-serif;font-weight:800;font-size:14px;line-height:20px;margin-top:14px}
.feature p{font-size:12px;line-height:16px;color:#d6deea;margin-top:8px}

/* brands */
.brand{top:2368px;font-family:"Montserrat",sans-serif;font-weight:800;font-size:22px;color:var(--navy);transform:translateX(-50%);letter-spacing:.5px}

/* footer */
.footer{left:0;top:2449px;width:1200px;height:377px;background:var(--sky);color:#fff}
.f-logo{left:133px;top:2482px;width:204px;height:204px;border-radius:50%;border:4px solid #fff;display:flex;flex-direction:column;align-items:center;justify-content:center;font-family:"Montserrat",sans-serif;font-weight:600;font-size:20px;letter-spacing:2px;color:#fff}
.f-col h4{font-family:"Montserrat",sans-serif;font-weight:800;font-size:14px;color:#fff;margin-bottom:8px}
.f-col a{display:block;font-size:13px;line-height:19.2px;color:#fff;text-decoration:none}
.email{left:825px;top:2517px;width:242px;height:44px;background:#fff;color:#333;font-size:12px;padding:14px 16px}
.sub-btn{left:825px;top:2575px;width:111px;height:40px;background:var(--navy);color:#fff;font-family:"Montserrat",sans-serif;font-weight:800;font-size:14px;display:flex;align-items:center;justify-content:center}
.social{top:2679px;width:27px;height:27px;border-radius:50%;border:2px solid #fff;background:rgba(255,255,255,.25)}
.f-rule{left:132px;top:2745px;width:937px;height:1px;background:#fff}
.copyright{left:0;top:2777px;width:1200px;text-align:center;font-size:12px;color:#fff}
</style>
</head>
<body>

<div class="abs topbar">
  <span><svg viewBox="0 0 24 24" fill="none" stroke="#4fb6f0" stroke-width="1.6"><rect x="2" y="6" width="12" height="10"/><path d="M14 9h4l3 4v3h-7"/><circle cx="7" cy="18" r="2"/><circle cx="17" cy="18" r="2"/></svg>Free Shipping Australia</span>
  <span><svg viewBox="0 0 24 24" fill="none" stroke="#4fb6f0" stroke-width="1.6"><path d="M3 20h18M6 16l4-8 4 3 4-7"/></svg>Buy Now, Pay Later, Splitpay</span>
  <span><svg viewBox="0 0 24 24" fill="none" stroke="#4fb6f0" stroke-width="1.6"><circle cx="12" cy="12" r="9"/><path d="M9 12l2 2 4-4"/></svg>60 Day Easy Returns</span>
</div>

<div class="abs header"></div>
<div class="abs logo-ring"></div>
<div class="abs logo"><span style="font-size:10px">POOL</span><span>HAVEN</span></div>
<div class="abs search">Search</div>
<div class="abs search-btn"><svg width="14" height="14" viewBox="0 0 24 24" fill="none" stroke="#fff" stroke-width="3"><circle cx="10" cy="10" r="6"/><path d="M15 15l5 5"/></svg></div>
<div class="abs shop-btn">SHOP FILTER CARTRIDGES</div>
<div class="abs login"><svg width="24" height="24" viewBox="0 0 24 24" fill="none" stroke="#1b3160" stroke-width="1.5"><circle cx="12" cy="12" r="10.5"/><circle cx="12" cy="9" r="3.5"/><path d="M5.5 19c1.5-3 4-4 6.5-4s5 1 6.5 4"/></svg>Login / Join</div>
<div class="abs divider"></div>
<div class="abs cart">CART <svg width="40" height="34" viewBox="0 0 40 34" fill="none" stroke="#1b3160" stroke-width="3"><path d="M2 4h6l5 20h20l4-14H11"/><circle cx="15" cy="30" r="2.5" fill="#1b3160"/><circle cx="30" cy="30" r="2.5" fill="#1b3160"/></svg></div>
<div class="abs cart-count">0</div>
<nav class="abs nav"><span>PUMPS</span><span>FILTERS</span><span>CHLORINATORS</span><span>CLEANERS</span><span>LIGHTS</span><span>MAINTENANCE</span><span>COVERS</span><span>HEATERS</span><span>SPAS</span><span>CHEMICALS</span></nav>

<section class="abs hero"></section>
<div class="abs hero-art" role="img" aria-label="Pool cleaning equipment, chlorine tablets bucket and test kit"></div>
<div class="abs hero-box">
  <h1>POOL STORE</h1>
  <p>Lorem Ipsum is simply dummy text<br>of the printing and typesetting.</p>
  <span class="hero-btn">SHOP NOW</span>
</div>
<div class="abs hero-arrow" style="left:0"><svg width="10" height="14" viewBox="0 0 10 14" fill="none" stroke="#fff" stroke-width="2"><path d="M7 1L2 7l5 6"/></svg></div>
<div class="abs hero-arrow" style="left:1169px"><svg width="10" height="14" viewBox="0 0 10 14" fill="none" stroke="#fff" stroke-width="2"><path d="M3 1l5 6-5 6"/></svg></div>

<h2 class="abs heading" style="left:0;top:643px;width:1200px">CATEGORIES</h2>

<div class="abs cat" style="left:131px;top:722px">Filter Cartridges ›<div class="thumb" role="img" aria-label="Filter cartridges" style="background:linear-gradient(90deg,#e8eef5,#b9c9dc)"></div></div>
<div class="abs cat" style="left:450px;top:722px">Pool Cleaners ›<div class="thumb" role="img" aria-label="Pool cleaner" style="background:linear-gradient(#f5d90a,#333)"></div></div>
<div class="abs cat" style="left:762px;top:722px">Pool Pumps ›<div class="thumb" role="img" aria-label="Pool pump" style="background:linear-gradient(#6b6f75,#2c2f33)"></div></div>
<div class="abs cat" style="left:131px;top:815px">Cleaning Equipment ›<div class="thumb" role="img" aria-label="Pool brush" style="background:linear-gradient(135deg,#dfeaf5,#3b7cc4)"></div></div>
<div class="abs cat" style="left:450px;top:815px">Pool Cleaner Spare Parts ›<div class="thumb" role="img" aria-label="Spare filter element" style="background:linear-gradient(#f3d88a,#c9a14a)"></div></div>
<div class="abs cat" style="left:762px;top:815px">Pool Chlorinators ›<div class="thumb" role="img" aria-label="Chlorinator unit" style="background:linear-gradient(#2f7fd6,#1a3a70)"></div></div>
<div class="abs cat" style="left:131px;top:908px">Pool &amp; Spa Chemicals ›<div class="thumb" role="img" aria-label="Chemical granules" style="background:radial-gradient(circle,#3fa3ee 40%,#e3edf6 62%)"></div></div>
<div class="abs cat" style="left:450px;top:908px">Pool Covers ›<div class="thumb" role="img" aria-label="Striped pool cover" style="background:linear-gradient(#2a6fd1,#dfe9f6)"></div></div>
<div class="abs cat" style="left:762px;top:908px">Skimmers &amp; Fittings ›<div class="thumb" role="img" aria-label="Skimmer lid" style="background:radial-gradient(circle,#35c0ee 45%,#fff 65%)"></div></div>
<div class="abs cat" style="left:131px;top:1002px">Pool Hoses ›<div class="thumb" role="img" aria-label="Foot pump and hose" style="background:linear-gradient(#f6cf1c,#2f6fd0)"></div></div>
<div class="abs cat" style="left:450px;top:1002px">Pool Heaters ›<div class="thumb" role="img" aria-label="Heater control panel" style="background:linear-gradient(#eef1f4,#c6ccd3)"></div></div>
<div class="abs cat" style="left:762px;top:1002px">Spa Parts ›<div class="thumb" role="img" aria-label="Spa tub" style="background:linear-gradient(#c9ced4,#4a3f3a)"></div></div>

<h2 class="abs heading" style="left:0;top:1138px;width:1200px">BEST SELLERS</h2>
<div class="abs circle-arrow" style="left:79px;top:1336px"><svg width="8" height="12" viewBox="0 0 8 12" fill="none" stroke="#1b3160" stroke-width="1.8"><path d="M6 1L2 6l4 5"/></svg></div>
<div class="abs circle-arrow" style="left:1090px;top:1336px"><svg width="8" height="12" viewBox="0 0 8 12" fill="none" stroke="#1b3160" stroke-width="1.8"><path d="M2 1l4 5-4 5"/></svg></div>

<div class="abs card" style="left:132px;top:1211px"><div class="pimg" role="img" aria-label="Sand filter with valve" style="background:linear-gradient(#f1f1ec,#2b2b2b)"></div><p class="pname">Lorem Ipsum is sim<br>ply dummy text</p><p class="price">$589.99</p><span class="add">Add to Cart</span></div>
<div class="abs card" style="left:320px;top:1211px"><div class="pimg" role="img" aria-label="Pool pump" style="background:linear-gradient(#8a8d91,#2f3236)"></div><p class="pname">Lorem Ipsum is sim<br>ply dummy text</p><p class="price">$589.99</p><span class="add">Add to Cart</span></div>
<div class="abs card" style="left:509px;top:1211px"><div class="pimg" role="img" aria-label="Submersible pump" style="background:linear-gradient(#f7dd14,#3a3a3a)"></div><p class="pname">Lorem Ipsum is sim<br>ply dummy text</p><p class="price">$589.99</p><span class="add">Add to Cart</span></div>
<div class="abs card" style="left:699px;top:1211px"><div class="pimg" role="img" aria-label="Water softener unit" style="background:linear-gradient(#6a7077,#2e8be0)"></div><p class="pname">Lorem Ipsum is sim<br>ply dummy text</p><p class="price">$589.99</p><span class="add">Add to Cart</span></div>
<div class="abs card" style="left:889px;top:1211px"><div class="pimg" role="img" aria-label="Chemical container" style="background:linear-gradient(#a7a6e8,#d7d6f4)"></div><p class="pname">Lorem Ipsum is sim<br>ply dummy text</p><p class="price">$589.99</p><span class="add">Add to Cart</span></div>

<h2 class="abs heading" style="left:0;top:1557px;width:1200px">LATEST PRODUCTS</h2>
<div class="abs circle-arrow" style="left:79px;top:1755px"><svg width="8" height="12" viewBox="0 0 8 12" fill="none" stroke="#1b3160" stroke-width="1.8"><path d="M6 1L2 6l4 5"/></svg></div>
<div class="abs circle-arrow" style="left:1090px;top:1755px"><svg width="8" height="12" viewBox="0 0 8 12" fill="none" stroke="#1b3160" stroke-width="1.8"><path d="M2 1l4 5-4 5"/></svg></div>

<div class="abs card" style="left:132px;top:1630px"><div class="pimg" role="img" aria-label="Multiport valve" style="background:linear-gradient(90deg,#2b2b2b,#e9e6dc)"></div><p class="pname">Lorem Ipsum is sim<br>ply dummy text</p><p class="price">$589.99</p><span class="add">Add to Cart</span></div>
<div class="abs card" style="left:320px;top:1630px"><div class="pimg" role="img" aria-label="Swimming goggles" style="background:linear-gradient(#fff,#cfe3f6 50%,#fff)"></div><p class="pname">Lorem Ipsum is sim<br>ply dummy text</p><p class="price">$589.99</p><span class="add">Add to Cart</span></div>
<div class="abs card" style="left:509px;top:1630px"><div class="pimg" role="img" aria-label="Pool float cushion" style="background:linear-gradient(#f4f4f4,#dcdcdc)"></div><p class="pname">Lorem Ipsum is sim<br>ply dummy text</p><p class="price">$589.99</p><span class="add">Add to Cart</span></div>
<div class="abs card" style="left:699px;top:1630px"><div class="pimg" role="img" aria-label="White chemical bottle" style="background:linear-gradient(#f2f2f2,#c9c9c9)"></div><p class="pname">Lorem Ipsum is sim<br>ply dummy text</p><p class="price">$589.99</p><span class="add">Add to Cart</span></div>
<div class="abs card" style="left:889px;top:1630px"><div class="pimg" role="img" aria-label="Freestanding bath" style="background:linear-gradient(#fff,#e6e6e6 60%,#c8a35a)"></div><p class="pname">Lorem Ipsum is sim<br>ply dummy text</p><p class="price">$589.99</p><span class="add">Add to Cart</span></div>

<section class="abs features"></section>
<div class="abs feature" style="left:125px;top:2007px">
  <svg width="70" height="52" viewBox="0 0 70 52" fill="none" stroke="#2ea7ea" stroke-width="3"><path d="M18 6h30v30H18M48 16h10l8 10v10H48"/><circle cx="28" cy="40" r="6"/><circle cx="56" cy="40" r="6"/><path d="M4 16h12M8 24h10M2 32h14"/></svg>
  <h3>FREE SHIPPING<br>AUSTRALIA WIDE</h3>
  <p>There are many variations of passages of Lorem Ipsum available, but the majority have suffered alteration in some form.</p>
</div>
<div class="abs feature" style="left:370px;top:2007px">
  <svg width="52" height="52" viewBox="0 0 52 52" fill="none" stroke="#2ea7ea" stroke-width="3"><path d="M10 28V22a16 16 0 0 1 32 0v6"/><rect x="6" y="26" width="8" height="14" rx="3"/><rect x="38" y="26" width="8" height="14" rx="3"/><path d="M42 40c0 6-6 8-14 8"/><circle cx="26" cy="48" r="3"/></svg>
  <h3>LIFETIME<br>AFTER-SALES SUPPORT</h3>
  <p>There are many variations of passages of Lorem Ipsum available, but the majority have suffered alteration in some form.</p>
</div>
<div class="abs feature" style="left:617px;top:2007px">
  <svg width="60" height="52" viewBox="0 0 60 52" fill="none" stroke="#2ea7ea" stroke-width="3"><path d="M14 4h32l12 14-28 32L2 18z"/><path d="M2 18h56M22 4l-6 14 14 32 14-32-6-14"/></svg>
  <h3>GAME-CHANGING<br>VALUE</h3>
  <p>There are many variations of passages of Lorem Ipsum available, but the majority have suffered alteration in some form.</p>
</div>
<div class="abs feature" style="left:865px;top:2007px">
  <svg width="54" height="54" viewBox="0 0 54 54" fill="none" stroke="#2ea7ea" stroke-width="3"><path d="M8 20A22 22 0 1 1 6 32"/><path d="M4 10v10h10"/><circle cx="27" cy="27" r="12"/><path d="M22 27l5-5 5 5-5 5z"/></svg>
  <h3>60 DAY<br>RETURNS</h3>
  <p>There are many variations of passages of Lorem Ipsum available, but the majority have suffered alteration in some form.</p>
</div>

<h2 class="abs heading" style="left:0;top:2270px;width:1200px">OUR BRANDS</h2>
<div class="abs" style="left:96px;top:2374px"><svg width="10" height="14" viewBox="0 0 10 14" fill="none" stroke="#1b3160" stroke-width="2"><path d="M7 1L2 7l5 6"/></svg></div>
<div class="abs" style="left:1099px;top:2374px"><svg width="10" height="14" viewBox="0 0 10 14" fill="none" stroke="#1b3160" stroke-width="2"><path d="M3 1l5 6-5 6"/></svg></div>
<span class="abs brand" style="left:216px">MARLIN</span>
<span class="abs brand" style="left:412px">CLEARWAVE</span>
<span class="abs brand" style="left:602px">LUMO</span>
<span class="abs brand" style="left:804px">TIDEWELL</span>
<span class="abs brand" style="left:999px">AQUAREX</span>

<footer class="abs footer"></footer>
<div class="abs f-logo"><span style="font-size:16px">POOL</span><span>HAVEN</span></div>
<div class="abs f-col" style="left:392px;top:2480px"><h4>PRODUCTS</h4><a>Pumps</a><a>Filters</a><a>Chlorinators</a><a>Cleaners</a><a>Lights</a><a>Maintenance</a><a>Covers</a><a>Heaters</a><a>Spas</a><a>Chemicals</a></div>
<div class="abs f-col" style="left:552px;top:2480px"><h4>ABOUT</h4><a>About us</a><a>Reviews</a><a>Blog</a><a>Free Quote</a></div>
<div class="abs f-col" style="left:691px;top:2480px"><h4>SUPPORT</h4><a>Shipping</a><a>Returns</a><a>Payment</a><a>Splitpay</a></div>
<div class="abs f-col" style="left:825px;top:2480px"><h4>SUBSCRIBE</h4></div>
<div class="abs email">Email Address</div>
<div class="abs sub-btn">SUBSCRIBE</div>
<div class="abs f-col" style="left:825px;top:2651px"><h4>FOLLOW US</h4></div>
<div class="abs social" style="left:824px" aria-label="Social profile"></div>
<div class="abs social" style="left:867px" aria-label="Social profile"></div>
<div class="abs social" style="left:909px" aria-label="Social profile"></div>
<div class="abs f-rule"></div>
<p class="abs copyright">Copyright © 2022 All Rights Reserved</p>

</body>
</html>
```